Online Prescription Eyeglass Lens Company Needs a Website

*Update new name to Glintwell. Thx

We are eye doctors with a lab that need a website for a new company based in Southern California called Glintwell. We replace old prescription lenses with new ones next day for most lenses. Patients select the lenses and give us the prescription. We then send a box with a prepaid shipping label. Place the frames in the box and drop them in the mail to our lab. We will custom make new lenses, fit them back into your frames and send them back to you. We would like to compete with www.spectrafold.com and offer affordable lenses for single vision, bifocal, progressive, sunglass lenses at an affordable price with next day shipping.
Updates

Hi Designers, We have a new name called Glintwell. Can we have the website design reflect the new name and we'll pick our favorites. Thx

Update: The new name is Brightmoor . I have not made very many changes or feedback to the submissions because we were bidding for a .com. We won and our new name is Brightmoor . This is the last name change.. Please have the website reflect the new name and I'll be providing feedback on the websites . ( I have a separate project for the logo people are working on, so don't worry about creating a logo). Look forward to the submissions. Thanks everyone.

Hi, Just leave the name as Glintwell for now. I will narrow down top designs tonight. Thx

Target Market(s)

Anyone that wears prescription or nonprescription glasses or sunglasses that want next day shipping.

Industry/Entity Type

Eyewear

Number of Pages Required

4 page

Font styles to use
Serif

Colors

Designer to choose colors to be used in the design.

Requirements
Must have
• I need a website that can compete with https://www.spectrafold.com/.
• We are different from spectrafold because we can offer same day service or next day shipping.
• It needs to have website that offers the lenses available listed below.
• Needs to be able to upload a prescription and payment feature.
• Pictures of different types of options with small info about each lens option.
• Template Pricing (just use numbers from $79-$179 for now)
• SINGLE VISION LENSES
• HIGH INDEX LENSES
• READING LENSES
• DIGITAL HD PROGRESSIVE LENSES
• RX & NON-RX SUNGLASSES
• RX & NON-RX POLARIZED SUNGLASSES
• COMPUTER LENSES
• TRANSITION LENSES
• BI-FOCAL LENSES

```html
<!DOCTYPE html>
<html lang="en">
<head>
<meta charset="utf-8">
<title>Glintwell – Prescription Lenses</title>
<link href="https://fonts.googleapis.com/css2?family=Open+Sans:wght@400;600;700&family=Orbitron:wght@500;700&display=swap" rel="stylesheet">
<style>
:root{
  --orange:#e2601f;
  --orange-light:#ee7d40;
  --orange-deep:#d9561a;
  --ink:#1b1d2a;
  --navy:#2a2f45;
  --grey-text:#7d7d7d;
  --muted:#a8a8a8;
  --soft-bg:#f5f5f5;
  --footer-bg:#efeff1;
  --card-bg:#dcdce0;
  --white:#ffffff;
}
*{margin:0;padding:0;box-sizing:border-box}
html,body{width:1200px;height:2321px;overflow:hidden}
body{position:relative;font-family:"Open Sans",Arial,sans-serif;color:var(--ink);background:var(--white)}
.display{font-family:"Orbitron","Arial Black",sans-serif;letter-spacing:4px;text-transform:uppercase}

/* Header */
.site-header{position:absolute;left:0;top:0;width:1200px;height:62px;background:var(--white);box-shadow:0 2px 6px rgba(0,0,0,.12);z-index:2}
.brand{position:absolute;left:160px;top:12px;font-size:30px;font-weight:600;color:var(--navy);letter-spacing:1px;line-height:38px}
.main-nav{position:absolute;left:472px;top:24px;display:flex;gap:30px}
.main-nav a{font-size:11px;font-weight:600;color:var(--muted);text-decoration:none;letter-spacing:.2px}
.header-divider{position:absolute;left:880px;top:0;width:1px;height:62px;background:#e2e2e2}
.header-icons{position:absolute;left:910px;top:18px;display:flex;gap:20px}

/* Hero */
.hero{position:absolute;left:0;top:62px;width:1200px;height:466px;
  background:
    radial-gradient(ellipse 260px 300px at 560px 260px,rgba(196,140,105,.85) 0%,rgba(150,100,70,.55) 45%,rgba(110,80,55,0) 100%),
    radial-gradient(ellipse 340px 230px at 600px 470px,rgba(60,40,40,.75) 0%,rgba(60,40,40,0) 100%),
    radial-gradient(ellipse at 50% 40%,#7d8473 0%,#60665a 55%,#3e4239 100%);}
.tagline-band{position:absolute;left:0;top:528px;width:1200px;height:114px;
  background:linear-gradient(115deg,var(--orange-deep) 0%,var(--orange-light) 30%,var(--orange) 55%,var(--orange-light) 80%,var(--orange-deep) 100%);
  display:flex;align-items:center;justify-content:center;text-align:center}
.tagline-band p{color:var(--white);font-size:25px;font-weight:600;line-height:31px}

/* Steps */
.steps{position:absolute;left:0;top:642px;width:1200px;height:361px;background:var(--soft-bg)}
.step{position:absolute;top:62px;width:252px;text-align:center}
.step-art{height:155px;margin:0 auto;border-bottom:2px solid var(--ink);display:flex;align-items:flex-end;justify-content:center}
.step-art span{display:block;width:200px;height:148px;border-radius:40px 40px 0 0;
  background:
    radial-gradient(ellipse 50px 60px at 70px 70px,rgba(214,88,70,.9) 0%,rgba(214,88,70,0) 100%),
    radial-gradient(ellipse 70px 55px at 140px 110px,rgba(232,192,120,.95) 0%,rgba(232,192,120,0) 100%),
    linear-gradient(180deg,#f1efec 0%,#e6e1da 100%);}
.step-art .mailbox{width:150px;border-radius:30px 30px 0 0;
  background:
    radial-gradient(ellipse 70px 40px at 65px 70px,rgba(206,32,32,.95) 0%,rgba(206,32,32,0) 100%),
    linear-gradient(180deg,#eeeeee 0%,#e2e2e2 100%);}
.step-badge{display:inline-block;margin-top:33px;background:var(--orange);color:var(--white);font-size:10px;font-weight:600;padding:5px 12px;letter-spacing:.3px}
.step-name{margin-top:11px;font-size:14px;font-weight:600}

/* Products */
.products{position:absolute;left:0;top:1003px;width:1200px;height:423px;background:var(--white)}
.section-rule{position:absolute;left:587px;top:50px;width:26px;height:2px;background:var(--orange)}
.eyebrow{position:absolute;left:0;width:1200px;top:66px;text-align:center;font-size:10px;color:var(--muted);letter-spacing:.5px}
.products h2{position:absolute;left:0;width:1200px;top:92px;text-align:center;font-size:21px;font-weight:500;color:var(--ink)}
.product{position:absolute;top:146px;width:204px;text-align:center}
.product-photo{width:204px;height:139px;background:var(--card-bg)}
.ph-dark{background:radial-gradient(ellipse 70px 28px at 50% 50%,#55555a 0%,#8d8d92 50%,var(--card-bg) 100%)}
.ph-tort{background:radial-gradient(ellipse 72px 26px at 50% 50%,#9a8580 0%,#c3b8b6 55%,var(--card-bg) 100%)}
.ph-grey{background:radial-gradient(ellipse 72px 28px at 50% 50%,#7a7a7d 0%,#a9a9ac 55%,var(--card-bg) 100%)}
.ph-avi{background:radial-gradient(ellipse 72px 28px at 50% 50%,#9aa0b2 0%,#c7c9d2 55%,var(--card-bg) 100%)}
.product h3{margin-top:23px;font-size:12.5px;font-weight:700;color:var(--ink)}
.product p{margin-top:6px;font-size:10.5px;line-height:17px;color:var(--grey-text)}
.arrow-tab{position:absolute;top:181px;width:26px;height:70px}

/* Promo */
.promo{position:absolute;left:0;top:1426px;width:1200px;height:320px;background:radial-gradient(ellipse at 60% 50%,#353535 0%,#1e1e1e 60%,#111 100%)}
.promo-glasses{position:absolute;left:121px;top:76px;width:380px;height:154px;border-radius:24px 60px 70px 40px;
  background:
    radial-gradient(ellipse 85px 62px at 220px 80px,#2a1f92 0%,rgba(42,31,146,.85) 55%,rgba(42,31,146,0) 100%),
    radial-gradient(ellipse 70px 60px at 330px 75px,#2a1f92 0%,rgba(42,31,146,.8) 55%,rgba(42,31,146,0) 100%),
    linear-gradient(90deg,rgba(201,106,37,.6) 0%,#e8782a 40%,#ef8a38 100%);}
.promo-copy{position:absolute;left:540px;width:508px;top:0;text-align:center}
.promo-rule{position:absolute;left:243px;top:82px;width:26px;height:2px;background:var(--orange)}
.promo-kicker{position:absolute;left:0;width:508px;top:101px;font-size:13px;font-weight:600;color:var(--white);letter-spacing:.3px}
.promo-title{position:absolute;left:0;width:508px;top:134px;font-size:28px;font-weight:700;color:var(--white);letter-spacing:5px}
.btn-outline{position:absolute;left:198px;top:196px;width:112px;height:42px;border:1px solid var(--orange);color:var(--orange);font-size:11px;font-weight:600;display:flex;align-items:center;justify-content:center;letter-spacing:.3px}

/* Info */
.about{position:absolute;left:160px;top:1784px;width:880px}
.about h4{font-size:14px;font-weight:700;color:var(--ink)}
.about p{margin-top:16px;font-size:11.2px;line-height:19px;color:var(--grey-text)}
.about p+p{margin-top:13px}

/* Newsletter */
.newsletter{position:absolute;left:0;top:1983px;width:1200px;height:62px;background:var(--orange)}
.newsletter h5{position:absolute;left:160px;top:18px;font-size:18px;font-weight:700;color:var(--white);letter-spacing:4.6px}
.newsletter .field{position:absolute;left:531px;top:13px;width:382px;height:35px;background:var(--white);font-size:10.5px;color:#777;padding:11px 12px}
.newsletter .btn{position:absolute;left:927px;top:13px;width:113px;height:35px;border:1.5px solid var(--white);color:var(--white);font-size:11px;font-weight:600;display:flex;align-items:center;justify-content:center}

/* Footer */
.site-footer{position:absolute;left:0;top:2045px;width:1200px;height:220px;background:var(--footer-bg)}
.footer-brand{position:absolute;left:160px;top:38px;font-size:30px;font-weight:600;color:var(--navy);letter-spacing:1px}
.footer-about{position:absolute;left:160px;top:89px;width:330px;font-size:10.5px;line-height:15px;color:var(--grey-text)}
.footer-col{position:absolute;top:42px}
.footer-col h6{font-size:13px;font-weight:600;color:var(--ink)}
.footer-links{list-style:none;margin-top:14px}
.footer-links li{font-size:10.5px;color:var(--grey-text);line-height:22.5px}
.footer-links li.active{color:var(--ink)}
.footer-links li::before{content:"›";margin-right:7px;color:var(--ink);font-weight:700}
.contact-row{display:flex;gap:12px;align-items:flex-start;margin-top:14px;font-size:10.5px;line-height:15px;color:var(--grey-text)}
.contact-row.tel{color:var(--ink)}
.contact-row.mail{color:var(--orange)}

/* Bottom bar */
.bottom-bar{position:absolute;left:0;top:2265px;width:1200px;height:56px;background:var(--white)}
.copyright{position:absolute;left:160px;top:21px;font-size:10.5px;color:var(--grey-text)}
.copyright b{color:var(--ink);font-weight:600}
.social{position:absolute;left:908px;top:16px;display:flex;gap:4px}
.social span{width:23px;height:23px;border-radius:50%}
</style>
</head>
<body>

<header class="site-header">
  <div class="brand">Glintwell</div>
  <nav class="main-nav">
    <a>OUR LENSES</a><a>WHY GLINTWELL</a><a>THE LAB</a><a>OUR PROCESS</a>
  </nav>
  <div class="header-divider"></div>
  <div class="header-icons">
    <svg width="20" height="22" viewBox="0 0 20 22"><circle cx="8" cy="9" r="6" fill="none" stroke="#222" stroke-width="2"/><line x1="12.5" y1="13.5" x2="17" y2="18" stroke="#222" stroke-width="2.2" stroke-linecap="round"/></svg>
    <svg width="24" height="24" viewBox="0 0 24 24"><path d="M4 7h12l-1 13H5z" fill="none" stroke="#222" stroke-width="1.8"/><path d="M7 7V5a3 3 0 0 1 6 0v2" fill="none" stroke="#222" stroke-width="1.8"/><circle cx="17" cy="18" r="5" fill="var(--orange)"/></svg>
    <svg width="22" height="22" viewBox="0 0 22 22"><circle cx="11" cy="7" r="4.5" fill="none" stroke="#222" stroke-width="1.8"/><path d="M3 20c0-4.5 3.6-7 8-7s8 2.5 8 7" fill="none" stroke="#222" stroke-width="1.8"/></svg>
  </div>
</header>

<section class="hero" role="img" aria-label="Photo of a smiling woman in large red glasses raising one finger"></section>

<section class="tagline-band">
  <p>Anyone that wears prescription or nonprescription glasses<br>or sunglasses that want next day shipping.</p>
</section>

<section class="steps">
  <div class="step" style="left:157px">
    <div class="step-art"><span role="img" aria-label="Illustration of a person selecting lenses at a computer desk"></span></div>
    <div class="step-badge">STEP ONE</div>
    <div class="step-name">Select Leanse</div>
  </div>
  <div class="step" style="left:472px">
    <div class="step-art"><span class="mailbox" role="img" aria-label="Illustration of a red mailbox with letters"></span></div>
    <div class="step-badge">STEP TWO</div>
    <div class="step-name">Send Prescreption</div>
  </div>
  <div class="step" style="left:784px">
    <div class="step-art"><span role="img" aria-label="Illustration of a person at a desk wearing new glasses"></span></div>
    <div class="step-badge">STEP THREE</div>
    <div class="step-name">New Lense</div>
  </div>
</section>

<section class="products">
  <div class="section-rule"></div>
  <div class="eyebrow">WE SELL LENSE</div>
  <h2 class="display">Our Products</h2>

  <article class="product" style="left:158px">
    <div class="product-photo ph-dark" role="img" aria-label="Black sunglasses"></div>
    <h3>SINGLE VISION LENSES</h3>
    <p>Single vision lenses are prescribed if<br>you need correction...</p>
  </article>
  <article class="product" style="left:384px">
    <div class="product-photo ph-tort" role="img" aria-label="Tortoise frame eyeglasses"></div>
    <h3>HIGH INDEX LENSES</h3>
    <p>Single vision lenses are prescribed if<br>you need correction...</p>
  </article>
  <article class="product" style="left:610px">
    <div class="product-photo ph-grey" role="img" aria-label="Grey tinted metal frame glasses"></div>
    <h3>READING LENSES</h3>
    <p>Single vision lenses are prescribed if<br>you need correction...</p>
  </article>
  <article class="product" style="left:836px">
    <div class="product-photo ph-avi" role="img" aria-label="Aviator sunglasses"></div>
    <h3>DIGITAL HD PROGRESSIVE</h3>
    <p>Single vision lenses are prescribed if<br>you need correction...</p>
  </article>

  <svg class="arrow-tab" style="left:158px" viewBox="0 0 26 70"><path d="M0 0L18 35L0 70z" fill="#fff"/><path d="M12 30l-5 5 5 5" fill="none" stroke="#222" stroke-width="1.8"/></svg>
  <svg class="arrow-tab" style="left:1014px" viewBox="0 0 26 70"><path d="M26 0L8 35L26 70z" fill="#fff"/><path d="M14 30l5 5-5 5" fill="none" stroke="#222" stroke-width="1.8"/></svg>
</section>

<section class="promo">
  <div class="promo-glasses" role="img" aria-label="Orange sunglasses with blue lenses"></div>
  <div class="promo-copy">
    <div class="promo-rule"></div>
    <div class="promo-kicker">SUNGLASSES THAT WANT NEXT DAY SHIPPING</div>
    <div class="promo-title display">Prescription Glasses</div>
    <a class="btn-outline">SHOP NOW</a>
  </div>
</section>

<section class="about">
  <h4>Information About Glintwell</h4>
  <p>Lorem ipsum dolor sit amet, consectetur adipiscing elit, sed do eiusmod tempor incididunt ut labore et dolore magna aliqua. Ut enim ad minim veniam, quis nostrud exercitation ullamco laboris nisi ut aliquip ex ea commodo consequat. Duis aute irure dolor in reprehenderit in voluptate velit esse cillum dolore eu fugiat nulla pariatur. Excepteur sint occaecat cupidatat non proident, sunt in culpa qui officia deserunt mollit anim id est laborum.</p>
  <p>Ut enim ad minim veniam, quis nostrud exercitation ullamco laboris nisi ut aliquip ex ea commodo consequat. Duis aute irure dolor in reprehenderit in voluptate velit esse cillum dolore eu fugiat nulla pariatur. Excepteur sint occaecat cupidatat non proident, sunt in culpa qui officia deserunt mollit anim id est laborum.</p>
</section>

<section class="newsletter">
  <h5 class="display">Newsletter Sign Up</h5>
  <div class="field">Enter Your email :</div>
  <div class="btn">SUBSCRIBE</div>
</section>

<footer class="site-footer">
  <div class="footer-brand">Glintwell</div>
  <p class="footer-about">Lorem ipsum dolor sit amet, consectetur adipiscing elit, sed do eiusmod tempor incididunt ut labore et dolore magna aliqua. Ut enim ad minim veniam, quis nostrud exercitation ullamco laboris nisi ut aliquip ex ea commodo consequat.</p>

  <div class="footer-col" style="left:573px">
    <h6>NAVIGATION</h6>
    <ul class="footer-links">
      <li class="active">Home</li><li>Products</li><li>Blogs</li><li>Contact Us</li>
    </ul>
  </div>

  <div class="footer-col" style="left:803px">
    <h6>CONTACT US</h6>
    <div class="contact-row">
      <svg width="12" height="17" viewBox="0 0 12 17"><path d="M6 0a6 6 0 0 0-6 6c0 4.5 6 11 6 11s6-6.5 6-11a6 6 0 0 0-6-6z" fill="#222"/><circle cx="6" cy="6" r="2.2" fill="var(--footer-bg)"/></svg>
      <span>Lorem ipsum dolor sit amet,<br>consectetur adipiscing elit, sed do</span>
    </div>
    <div class="contact-row tel">
      <svg width="12" height="14" viewBox="0 0 12 14"><path d="M3 1l2 3-1.5 1.5a8 8 0 0 0 4 4L9 8l3 2-1.5 3C6 13 0 7 1 2.5z" fill="#222"/></svg>
      <span>012 3456 789</span>
    </div>
    <div class="contact-row mail">
      <svg width="16" height="13" viewBox="0 0 16 13"><path d="M1 5l7-4 7 4v7H1z" fill="none" stroke="var(--orange)" stroke-width="1.3"/><path d="M1 5l7 4 7-4" fill="none" stroke="var(--orange)" stroke-width="1.3"/></svg>
      <span>info@glintwell-mail.com</span>
    </div>
  </div>
</footer>

<div class="bottom-bar">
  <p class="copyright">© Copyright 2017 <b>Glintwell.</b> All Rights Reserved.</p>
  <div class="social" aria-label="Social links">
    <span style="background:#3b5a9a"></span><span style="background:#2aa3ef"></span><span style="background:#d42d27"></span><span style="background:#1b78b5"></span><span style="background:#c9623f"></span>
  </div>
</div>

</body>
</html>
```